Olive oil labels

We are a small company of traditional products Olive oil, honey, pollen and various liqueurs and we would like to create an appealing and elegant label for our olive oil.
Use the Vardomar logo. Design #: 4358934
Can or can not use the Castle.
Can be one or two labels (front and back)
Have to have all the text.
- Azeite Virgem Extra - In great prominence
- Azeite de categoria superior obtido diretamente de azeitonas, unicamente por processo mecânico.
- Edição Limitada
- produzido e embalado por BLT
- consumir preferência antes do fim de
- Lote
- Vilarinho-Fontelas | Trás-os-Montes
- Portugal
- vardomar.lda@quintamail.example
(It has various sizes * 250ml (w4cmXh11cm)* 500ml (w9cmxh7) *750ml (w7xh13) *5L (w12cmxh14cm)

Target Market(s)

People with money expensive product but very good and in small quantity.

Industry/Entity Type

It Company

Font styles to use
Serif
Script

Colors

Designer to choose colors to be used in the design.

Requirements
Must have
• The tower of Fontelas - attached image
Nice to have
• Maybe have written extra virgin olive oil in Portuguese " Azeite Virgem Extra" and English .
• Black label preference.

```html
<!DOCTYPE html>
<html lang="pt">
<head>
<meta charset="utf-8">
<title>Vardomar – Azeite Virgem Extra label</title>
<link rel="stylesheet" href="https://fonts.googleapis.com/css2?family=Cormorant+Garamond:ital,wght@0,400;0,500;0,600;1,500&display=swap">
<style>
  :root {
    --backdrop: #26241c;
    --paper: #ffffff;
    --royal-blue: #1f3f94;
    --royal-blue-deep: #142b6b;
    --royal-blue-light: #3a62c0;
    --gold: #c9a44e;
    --gold-soft: #dcc17f;
    --ink-blue: #2a4aa0;
    --olive: #8d9a2e;
    --olive-deep: #5f6b1a;
  }
  * { margin: 0; padding: 0; box-sizing: border-box; }
  html, body { width: 1200px; height: 771px; overflow: hidden; }
  body {
    background: var(--backdrop);
    font-family: "Cormorant Garamond", Georgia, serif;
    display: flex; align-items: center; justify-content: center;
  }
  .label {
    width: 262px; height: 708px;
    background: var(--paper);
    display: flex; flex-direction: column;
  }
  .label__brand {
    height: 200px;
    display: flex; flex-direction: column; align-items: center; justify-content: center;
    gap: 10px;
    border-bottom: 3px solid var(--gold);
  }
  .brand__dot {
    width: 58px; height: 58px; border-radius: 50%;
    background: var(--gold);
  }
  .brand__name {
    color: var(--ink-blue);
    font-size: 25px; font-weight: 500; letter-spacing: .5px;
    text-transform: uppercase;
  }
  .label__band {
    height: 252px;
    background: linear-gradient(180deg, var(--royal-blue-deep) 0%, var(--royal-blue) 45%, var(--royal-blue-light) 100%);
    border-bottom: 3px solid var(--gold);
    display: flex; flex-direction: column; align-items: center;
    padding-top: 12px; text-align: center;
  }
  .band__title {
    color: var(--paper);
    font-style: italic; font-weight: 500; font-size: 25px; line-height: 1.05;
  }
  .band__subtitle {
    color: var(--gold-soft);
    font-style: italic; font-weight: 500; font-size: 20px; line-height: 1.1;
  }
  .band__tower {
    width: 140px; height: 112px; margin-top: 12px;
    background: linear-gradient(180deg, rgba(255,255,255,.18), rgba(255,255,255,.05));
  }
  .band__origin {
    margin-top: 14px;
    color: var(--gold-soft);
    font-size: 9.5px; font-variant: small-caps; letter-spacing: .5px; line-height: 1.6;
  }
  .label__details {
    flex: 1;
    display: flex; flex-direction: column; align-items: center;
    text-align: center; padding: 0 26px 18px;
    position: relative;
  }
  .details__olives {
    width: 150px; height: 42px; margin-top: -6px;
    background: linear-gradient(90deg, var(--olive-deep), var(--olive), var(--olive-deep));
    border-radius: 20px;
  }
  .details__description {
    margin-top: 20px;
    color: var(--ink-blue);
    font-size: 8.5px; line-height: 1.3;
  }
  .details__edition {
    margin-top: 20px; width: 100%;
    border-top: 1px solid var(--gold); border-bottom: 1px solid var(--gold);
    padding: 6px 0;
    color: var(--gold);
    font-size: 10px; font-weight: 600; letter-spacing: .5px; text-transform: uppercase;
  }
  .details__producer {
    margin-top: 28px;
    color: var(--ink-blue);
    font-size: 8.5px; font-weight: 600; letter-spacing: .4px; text-transform: uppercase;
  }
  .details__email {
    margin-top: 20px;
    color: var(--gold);
    font-size: 10px;
  }
  .details__footer {
    position: absolute; left: 18px; right: 26px; bottom: 16px;
    display: flex; justify-content: space-between; align-items: baseline;
    color: var(--ink-blue);
  }
  .footer__volume { font-size: 15px; }
  .footer__lot { font-size: 7.5px; font-weight: 600; text-transform: uppercase; }
</style>
</head>
<body>
  <main class="label">
    <header class="label__brand">
      <span class="brand__dot"></span>
      <span class="brand__name">Vardomar</span>
    </header>

    <section class="label__band">
      <h1 class="band__title">Azeite Virgem Extra</h1>
      <p class="band__subtitle">Extra Virgin Olive Oil</p>
      <div class="band__tower" role="img" aria-label="Line drawing of the tower of Fontelas"></div>
      <p class="band__origin">Vilarinho-Fontelas | Trás-os-Montes<br>Portugal</p>
    </section>

    <section class="label__details">
      <div class="details__olives" role="img" aria-label="Illustration of two green olives on a leafy sprig"></div>
      <p class="details__description">Azeite de categoria superior obtido diretamente de azeitonas, unicamente por processo mecânico.</p>
      <p class="details__edition">Edição Limitada</p>
      <p class="details__producer">Produzido e embalado por BLT</p>
      <p class="details__email">vardomar.lda@quintamail.example</p>
      <div class="details__footer">
        <span class="footer__volume">250 ML</span>
        <span class="footer__lot">Lote</span>
      </div>
    </section>
  </main>
</body>
</html>
```